Email footer for a cafe

The task is to design an email footer for a new start up cafe business. The logo has been designed, but we would like a professional email footer to sign off on all emails.

The email footer should :
1. look professional and competent
2. be clean and easy to read
3. the email must have the ability to optimise / adjust across the bottom of the email depending on the device being used to read the email
4. the design may stretch across the entire bottom of the email, but this is not mandatory
5. it must incorporate the logo and the details as listed below.
6. For any additional lines / dividers that a designer might choose to incorporate into the email footer, our preference is to match the colour of the logo.

The logo is attached. The logo details are:

The CMYK for the logo is C0 M50 Y100 K0 in font BankGothic Lt BT - Light
The CMKY for the text is C75 M68 Y67 K89 in font AvantGarde Bk BT - Book

The details to be included in the email footer are:

Pim Arlow
Founder
0417 286 314
pimarlow@bramblekitchenvq.com
Unit 6, 14 Talvery Crescelt
Wexholm TLB 5162

Have fun and thank you in advance for choosing to work on our job.

Reason: Thank you to everyone who has submitted their designs for an email footer. Looking at the designs most have been designed horizontally. Could I please also see some designs where all the elements are under each other in a stacked format. I have attached 2 images which I have grabbed from the internet to be used as an example.

```html
<!DOCTYPE html>
<html lang="en">
<head>
<meta charset="utf-8">
<title>Bramble Kitchen – Email Footer</title>
<link href="https://fonts.googleapis.com/css2?family=Questrial&family=Syncopate&display=swap" rel="stylesheet">
<style>
  :root {
    --stage: #5c5c5c;
    --paper: #fdfaf4;
    --brand-orange: #f7941d;
    --ink: #1b1a1a;
    --white: #ffffff;
  }
  html, body {
    margin: 0;
    padding: 0;
    width: 1200px;
    height: 1000px;
    overflow: hidden;
    background: var(--stage);
  }
  .canvas {
    position: relative;
    width: 1200px;
    height: 1000px;
  }
  .signature {
    position: absolute;
    left: 402px;
    top: 200px;
    width: 396px;
    height: 600px;
    background: var(--paper);
    border: 1px solid var(--brand-orange);
    box-sizing: border-box;
    font-family: "Questrial", "Century Gothic", sans-serif;
    color: var(--ink);
  }
  .signature__body {
    padding: 50px 36px 0;
  }
  .sign-off {
    margin: 0 0 12px;
    font-size: 17px;
  }
  .name-line {
    margin: 0;
    display: flex;
    align-items: baseline;
    gap: 10px;
    font-size: 17px;
  }
  .name-line__name {
    font-family: "Syncopate", "Arial", sans-serif;
    color: var(--brand-orange);
    font-size: 21px;
    letter-spacing: 1px;
  }
  .name-line__divider {
    width: 3px;
    height: 22px;
    background: var(--ink);
    align-self: center;
  }
  .company-line {
    margin: 12px 0 22px;
    color: var(--brand-orange);
    font-size: 18px;
  }
  .contact-list {
    list-style: none;
    margin: 0;
    padding: 0;
  }
  .contact-list__item {
    display: flex;
    align-items: flex-start;
    gap: 10px;
    font-size: 17px;
    line-height: 21px;
    margin-bottom: 16px;
  }
  .contact-list__icon {
    flex: none;
    width: 20px;
    height: 20px;
    margin-top: 1px;
  }
  .brand-mark {
    position: absolute;
    left: 0;
    right: 0;
    top: 336px;
    display: flex;
    flex-direction: column;
    align-items: center;
    gap: 20px;
  }
  .brand-mark__dot {
    width: 40px;
    height: 40px;
    border-radius: 50%;
    background: var(--brand-orange);
  }
  .brand-mark__name {
    color: var(--brand-orange);
    font-size: 36px;
    line-height: 1;
  }
  .social-bar {
    position: absolute;
    left: 0;
    right: 0;
    bottom: 0;
    height: 86px;
    background: var(--brand-orange);
    display: flex;
    align-items: center;
    padding-left: 30px;
    gap: 16px;
  }
  .social-bar__link {
    width: 40px;
    height: 40px;
    border-radius: 8px;
    background: var(--white);
    display: flex;
    align-items: center;
    justify-content: center;
  }
  .social-bar__link svg {
    width: 28px;
    height: 28px;
  }
</style>
</head>
<body>
<main class="canvas">
  <section class="signature">
    <div class="signature__body">
      <p class="sign-off">Best Regards,</p>
      <p class="name-line">
        <span class="name-line__name">Pim Arlow</span>
        <span class="name-line__divider"></span>
        <span class="name-line__role">Founder</span>
      </p>
      <p class="company-line">Bramble Kitchen</p>
      <ul class="contact-list">
        <li class="contact-list__item">
          <svg class="contact-list__icon" viewBox="0 0 20 20" aria-hidden="true">
            <rect width="20" height="20" rx="3" fill="var(--brand-orange)"/>
            <path d="M10 3.5a4 4 0 0 0-4 4c0 3 4 8 4 8s4-5 4-8a4 4 0 0 0-4-4z" fill="var(--white)"/>
            <circle cx="10" cy="7.5" r="1.6" fill="var(--brand-orange)"/>
          </svg>
          <span>Unit 6, 14 Talvery Crescelt<br>Wexholm TLB 5162</span>
        </li>
        <li class="contact-list__item">
          <svg class="contact-list__icon" viewBox="0 0 20 20" aria-hidden="true">
            <rect width="20" height="20" rx="3" fill="var(--brand-orange)"/>
            <path d="M7 4h2.5l1 3.5-1.6 1.2a7 7 0 0 0 2.4 2.4l1.2-1.6 3.5 1v2.5c0 1-1 1.5-2 1.5A9 9 0 0 1 5.5 6c0-1 .5-2 1.5-2z" fill="var(--white)"/>
          </svg>
          <span>0417 286 314</span>
        </li>
        <li class="contact-list__item">
          <svg class="contact-list__icon" viewBox="0 0 20 20" aria-hidden="true">
            <rect width="20" height="20" rx="3" fill="var(--brand-orange)"/>
            <rect x="4" y="5.5" width="12" height="9" fill="var(--white)"/>
            <path d="M4 5.5l6 5 6-5" fill="none" stroke="var(--brand-orange)" stroke-width="1.2"/>
          </svg>
          <span>pimarlow@bramblekitchenvq.com</span>
        </li>
      </ul>
    </div>

    <div class="brand-mark">
      <span class="brand-mark__dot"></span>
      <span class="brand-mark__name">Bramble Kitchen</span>
    </div>

    <nav class="social-bar" aria-label="Links">
      <span class="social-bar__link" aria-label="Email">
        <svg viewBox="0 0 28 28" aria-hidden="true">
          <rect x="4" y="7" width="20" height="14" fill="none" stroke="var(--brand-orange)" stroke-width="2"/>
          <path d="M4 7l10 8 10-8" fill="none" stroke="var(--brand-orange)" stroke-width="2"/>
        </svg>
      </span>
      <span class="social-bar__link" aria-label="Website">
        <svg viewBox="0 0 28 28" aria-hidden="true">
          <g fill="none" stroke="var(--brand-orange)" stroke-width="1.8">
            <circle cx="14" cy="14" r="10"/>
            <ellipse cx="14" cy="14" rx="4.5" ry="10"/>
            <path d="M4 14h20M6 9h16M6 19h16"/>
          </g>
        </svg>
      </span>
      <span class="social-bar__link" aria-label="Location">
        <svg viewBox="0 0 28 28" aria-hidden="true">
          <path d="M14 3a7 7 0 0 0-7 7c0 5.5 7 15 7 15s7-9.5 7-15a7 7 0 0 0-7-7z" fill="var(--brand-orange)"/>
          <circle cx="14" cy="10" r="2.8" fill="var(--white)"/>
        </svg>
      </span>
      <span class="social-bar__link" aria-label="Share">
        <svg viewBox="0 0 28 28" aria-hidden="true">
          <path d="M9 14l10-6M9 14l10 6" stroke="var(--brand-orange)" stroke-width="2" fill="none"/>
          <circle cx="8" cy="14" r="3.5" fill="var(--brand-orange)"/>
          <circle cx="20" cy="7.5" r="3.5" fill="var(--brand-orange)"/>
          <circle cx="20" cy="20.5" r="3.5" fill="var(--brand-orange)"/>
        </svg>
      </span>
      <span class="social-bar__link" aria-label="Message">
        <svg viewBox="0 0 28 28" aria-hidden="true">
          <path d="M5 6h18a1 1 0 0 1 1 1v11a1 1 0 0 1-1 1H12l-5 4v-4H5a1 1 0 0 1-1-1V7a1 1 0 0 1 1-1z" fill="var(--brand-orange)"/>
        </svg>
      </span>
      <span class="social-bar__link" aria-label="Call">
        <svg viewBox="0 0 28 28" aria-hidden="true">
          <path d="M9 4h4l1.5 5-2.4 1.8a10 10 0 0 0 5.1 5.1L19 13.5l5 1.5v4c0 1.5-1.5 2.5-3 2.5A16 16 0 0 1 6.5 7c0-1.5 1-3 2.5-3z" fill="var(--brand-orange)"/>
        </svg>
      </span>
    </nav>
  </section>
</main>
</body>
</html>
```